Korvane Business Cards

We need a business card design. We are a Technology (Audio Visual) design, sales and installation company. Looking for a double sided design, clean

Contact Information for Business Card

Clean, modern look, 2 sided

Font styles to use
Sans Serif

```html
<!DOCTYPE html>
<html lang="en">
<head>
<meta charset="utf-8">
<title>Korvane Business Cards</title>
<link rel="stylesheet" href="https://fonts.googleapis.com/css2?family=Exo+2:wght@600;700&family=Open+Sans:wght@400;600&display=swap">
<style>
  :root {
    --navy: #1c3343;
    --navy-soft: #243f50;
    --orange: #f7941d;
    --grey: #8a8a8a;
    --ink: #1f3444;
    --white: #ffffff;
    --stage: #2a2a2a;
  }
  * { box-sizing: border-box; margin: 0; padding: 0; }
  html, body {
    width: 1200px; height: 900px; overflow: hidden;
    background: var(--stage);
  }
  .canvas {
    position: relative; width: 1200px; height: 900px;
  }
  .card {
    position: absolute; left: 280px; width: 640px; height: 366px;
    box-shadow: 0 10px 30px rgba(0,0,0,.45);
  }
  .card--front {
    top: 70px; background: var(--navy);
    display: flex; align-items: center; justify-content: center;
  }
  .card--back { top: 464px; background: var(--white); }

  .wordmark {
    font-family: "Exo 2", sans-serif; font-weight: 700;
    font-size: 60px; letter-spacing: -1px; line-height: 1;
  }
  .card--front .wordmark { color: var(--white); margin-left: 140px; }
  .card--back .wordmark {
    position: absolute; left: 40px; top: 36px; color: var(--ink); font-size: 56px;
  }

  .address {
    position: absolute; left: 420px; top: 104px;
    font-family: "Open Sans", sans-serif; font-size: 15px; line-height: 1.2;
    color: var(--grey); letter-spacing: .5px;
  }
  .holder {
    position: absolute; left: 412px; top: 196px;
    font-family: "Exo 2", sans-serif; font-weight: 600; font-size: 19px;
    color: var(--ink); letter-spacing: .5px; text-transform: uppercase;
  }
  .holder-rule {
    position: absolute; left: 408px; top: 240px;
    width: 14px; height: 2px; background: var(--orange);
  }
  .contacts {
    position: absolute; left: 402px; top: 270px; list-style: none;
    font-family: "Open Sans", sans-serif; font-size: 16px; line-height: 22px;
    color: var(--grey);
  }
  .contacts li { display: flex; align-items: center; gap: 8px; }
  .contacts svg { width: 14px; height: 14px; flex: none; }
  .contacts .accent { color: var(--orange); font-weight: 600; }
</style>
</head>
<body>
<main class="canvas">
  <section class="card card--front" aria-label="Card front">
    <div class="wordmark">Korvane</div>
  </section>

  <section class="card card--back" aria-label="Card back">
    <div class="wordmark">Korvane</div>
    <address class="address">
      1180 Larkspur Way<br>
      Suite 100<br>
      Alden, Georgia 30412
    </address>
    <h1 class="holder">Dana Whitfield</h1>
    <div class="holder-rule"></div>
    <ul class="contacts">
      <li>
        <svg viewBox="0 0 16 16" fill="none" stroke="#f7941d" stroke-width="1.4"><circle cx="8" cy="8" r="6.8"/><path d="M5.5 4.8c-.6.6-.4 2 .9 3.6 1.4 1.6 2.9 2.4 3.7 1.8l.7-.7-1.4-1.2-.8.6c-.6-.3-1.4-1.1-1.7-1.8l.6-.8L6.3 4.9z"/></svg>
        (555)204-3170
      </li>
      <li>
        <svg viewBox="0 0 16 16" fill="none" stroke="#f7941d" stroke-width="1.4"><rect x="1.5" y="3.5" width="13" height="9"/><path d="M1.5 3.5 8 9l6.5-5.5"/></svg>
        sales@korvane.tech
      </li>
      <li>
        <svg viewBox="0 0 16 16" fill="none" stroke="#f7941d" stroke-width="1.4"><circle cx="8" cy="8" r="6.5"/><ellipse cx="8" cy="8" rx="3" ry="6.5"/><path d="M1.5 8h13M2.5 4.8h11M2.5 11.2h11"/></svg>
        <span>www.<span class="accent">korvane</span>.tech</span>
      </li>
    </ul>
  </section>
</main>
</body>
</html>
```